K7 Solutions business card design contest. Use logo and create a professional layout.

See attached sample. Please sharpen all text and images, don't want any pix-elated content. We are looking for a clean look that quickly provides the information need. Please include our information provided on the sample card. Please feel free to offer any design changes. Please only user the colors provided: #2D3539 & #FFA500. Do not prefer any images other than the K7 Logo

Target Market(s)

Construction, Architects, General Contractors, residential

Industry/Entity Type

Business

Contact Information for Business Card

Company logo, Name, email, fax & phone

Font styles to use
Other font styles liked:
• Josefin Slab

Requirements
Must have
• Name
• Phone & Fax #'s
• address
• Logo
• Website url: www.kq7solutions.example
Nice to have
• Font Colors #2D3539 & #FFA400
• We prefer a white background.

```html
<!DOCTYPE html>
<html lang="en">
<head>
<meta charset="UTF-8">
<title>K7 Solutions – Business Card</title>
<link href="https://fonts.googleapis.com/css2?family=Montserrat:wght@400;500;600;700&display=swap" rel="stylesheet">
<style>
  :root {
    --orange: #f0962a;
    --orange-text: #f29b2e;
    --charcoal: #2d3539;
    --paper: #ffffff;
    --backdrop: #e4e4e4;
  }
  * { margin: 0; padding: 0; box-sizing: border-box; }
  html, body {
    width: 1200px; height: 852px; overflow: hidden;
    background: var(--backdrop);
    font-family: "Montserrat", Arial, sans-serif;
  }
  .stage { position: relative; width: 1200px; height: 852px; }

  .card {
    position: absolute;
    width: 560px; height: 320px;
    border-radius: 14px;
    overflow: hidden;
    box-shadow: 0 6px 18px rgba(0,0,0,0.18);
  }

  /* Front */
  .card-front {
    left: 110px; top: 90px;
    background: var(--orange);
    display: flex; align-items: center; justify-content: center;
  }
  .brand { display: flex; align-items: center; gap: 14px; color: var(--charcoal); }
  .brand-mark {
    width: 54px; height: 54px;
    border: 4px solid var(--charcoal);
    border-radius: 8px;
  }
  .brand-text { display: flex; flex-direction: column; }
  .brand-name { font-weight: 600; font-size: 40px; line-height: 1; letter-spacing: 0.5px; }
  .brand-tagline { font-weight: 600; font-size: 17px; margin-top: 4px; }

  /* Back */
  .card-back {
    left: 530px; top: 440px;
    background: var(--paper);
  }
  .card-back .brand { position: absolute; left: 40px; top: 70px; gap: 10px; }
  .card-back .brand-mark { width: 40px; height: 40px; border-width: 3px; border-radius: 6px; }
  .card-back .brand-name { font-size: 30px; }
  .card-back .brand-tagline { font-size: 13px; margin-top: 2px; }

  .contact {
    position: absolute; left: 320px; top: 52px;
    color: var(--charcoal);
  }
  .contact-name { color: var(--orange-text); font-size: 19px; font-weight: 400; }
  .contact-title { font-size: 13px; margin-top: 4px; }
  .contact-list { list-style: none; margin-top: 16px; font-size: 12.5px; line-height: 1.55; }
  .contact-list li { display: flex; align-items: center; gap: 8px; }
  .contact-list svg { width: 12px; height: 12px; flex: none; fill: var(--orange-text); }
  .contact-address { font-size: 12.5px; line-height: 1.55; margin-top: 2px; padding-left: 20px; }

  .services {
    position: absolute; left: 40px; bottom: 34px;
    color: var(--orange-text); font-size: 14px; letter-spacing: 0.5px;
  }
  .edge-band {
    position: absolute; left: 0; right: 0; bottom: 0; height: 9px;
    display: flex;
  }
  .edge-band .band-orange { flex: 4; background: var(--orange); }
  .edge-band .band-dark { flex: 1; background: var(--charcoal); }
</style>
</head>
<body>
<main class="stage">

  <section class="card card-front" aria-label="Card front">
    <div class="brand">
      <span class="brand-mark" aria-hidden="true"></span>
      <div class="brand-text">
        <span class="brand-name">K7 Solutions</span>
        <span class="brand-tagline">Clarity From Every Angle</span>
      </div>
    </div>
  </section>

  <section class="card card-back" aria-label="Card back">
    <div class="brand">
      <span class="brand-mark" aria-hidden="true"></span>
      <div class="brand-text">
        <span class="brand-name">K7 Solutions</span>
        <span class="brand-tagline">Clarity From Every Angle</span>
      </div>
    </div>

    <div class="contact">
      <p class="contact-name">Daniel R. Hale, MBA</p>
      <p class="contact-title">Director of Operations</p>
      <ul class="contact-list">
        <li>
          <svg viewBox="0 0 12 12" aria-hidden="true"><path d="M2.5 1h2l1 2.5-1.3 1a6 6 0 0 0 2.8 2.8l1-1.3 2.5 1v2a1 1 0 0 1-1 1A9 9 0 0 1 1.5 2a1 1 0 0 1 1-1z"/></svg>
          (555) 014 - 2093
        </li>
        <li>
          <svg viewBox="0 0 12 12" aria-hidden="true"><path d="M3 1h5v3H3zM1 5h10v5H9v1H3v-1H1zM4 8v2h4V8z"/></svg>
          (555) 017 - 4082
        </li>
        <li>
          <svg viewBox="0 0 12 12" aria-hidden="true"><circle cx="6" cy="6" r="5.5"/></svg>
          www.kq7solutions.example
        </li>
      </ul>
      <p class="contact-address">1270 Maple Ridge Road, Suite<br>210-118 Fairview, Georgia, 30099</p>
    </div>

    <p class="services">DRONE | WEBCAM | VIDEO</p>
    <div class="edge-band" aria-hidden="true">
      <span class="band-orange"></span>
      <span class="band-dark"></span>
    </div>
  </section>

</main>
</body>
</html>
```